sydney wedding photography business needs a business card design

we need a business card design for a sydney based wedding photography and videography business. our business name is :golden hour studios and film. our target clients are 24-35 yrs female. our style is candid, organic, natural, dynamic. we are a team of young photographers and videographers, and help brides to create memories that they will cherish for the rest of their lives. the logo will be provided. we want an elegant design that reflects our style, and also want to give a great impression to our clients that we are one of the best studios in sydney and our brand means quality and premium service.

Target Market(s)

bride to be, 24-35 years old, living in sydney and surrunding areas

Industry/Entity Type

Wedding Photography

Contact Information for Business Card

address: 47 marrowbank street, lilyfield nsw 2040
mobile: 0417283951
phone: (02) 9163 2748
info@goldenhourstudio.net.au
www.goldenhourstudio.net.au
facebook:goldenhourbridals
instagram:goldenhourbridals

Font styles to use
Serif
Sans Serif

Requirements
Nice to have
• maybe add my slogan"memories beyond eternity" if the layout looks good
Should not have
• no black color, not good idea for wedding biz card

```html
<!DOCTYPE html>
<html lang="en">
<head>
<meta charset="utf-8">
<title>Golden Hour Studios and Film – Business Card</title>
<link href="https://fonts.googleapis.com/css2?family=Open+Sans:wght@400;600&display=swap" rel="stylesheet">
<style>
  :root {
    --backdrop: #3b3531;
    --card-light: #fbf7ee;
    --card-warm: #efe6d3;
    --gold: #e0a800;
    --gold-deep: #b07d00;
    --gold-text: #a87700;
    --text-main: #4a3b2a;
    --decor: #e8dcc4;
    --rule: #c9a24a;
  }
  html, body {
    margin: 0;
    width: 1200px;
    height: 844px;
    overflow: hidden;
    background: var(--backdrop);
    font-family: "Open Sans", Arial, sans-serif;
  }
  .canvas {
    position: relative;
    width: 1200px;
    height: 844px;
  }
  .card {
    position: absolute;
    top: 268px;
    width: 540px;
    height: 310px;
    overflow: hidden;
    box-shadow: 0 12px 30px rgba(0,0,0,.45);
  }

  /* Contact side */
  .card--contact {
    left: 40px;
    background: linear-gradient(160deg, var(--card-light) 0%, var(--card-warm) 100%);
  }
  .gold-band {
    position: absolute;
    left: 0;
    width: 100%;
    height: 14px;
    background: linear-gradient(90deg, var(--gold-deep), var(--gold));
  }
  .gold-band--top { top: 0; }
  .gold-band--bottom { bottom: 0; }
  .ring-decor {
    position: absolute;
    left: 0;
    top: 60px;
    width: 190px;
    height: 236px;
    background: radial-gradient(ellipse at 45% 40%, var(--decor) 0%, rgba(232,220,196,.5) 55%, transparent 75%);
  }
  .contact-block {
    position: absolute;
    left: 170px;
    top: 36px;
    width: 330px;
    text-align: center;
    color: var(--text-main);
  }
  .person-name {
    display: inline-block;
    margin: 0;
    padding: 0 4px 3px;
    font-size: 17px;
    font-weight: 600;
    letter-spacing: .5px;
    color: var(--gold-text);
    border-bottom: 1px solid var(--rule);
  }
  .person-role {
    margin: 2px 0 14px;
    font-size: 12px;
  }
  .contact-line {
    margin: 0;
    font-size: 13px;
    line-height: 1.45;
  }
  .address-line {
    margin: 12px 0 10px;
    font-size: 13px;
  }
  .social-row {
    display: flex;
    justify-content: center;
    align-items: center;
    gap: 8px;
    font-size: 12px;
  }
  .social-dot {
    width: 14px;
    height: 14px;
    background: var(--gold);
  }
  .social-dot--round { border-radius: 50%; }
  .social-handle { margin-right: 6px; }

  /* Brand side */
  .card--brand {
    left: 620px;
    background: radial-gradient(ellipse at 50% 40%, var(--card-light) 0%, var(--card-warm) 75%);
  }
  .edge-tab {
    position: absolute;
    width: 22px;
    height: 44px;
    background: linear-gradient(180deg, var(--gold), var(--gold-deep));
  }
  .edge-tab::after {
    content: "";
    position: absolute;
    top: 0;
    width: 3px;
    height: 100%;
    background: #ffffff;
  }
  .edge-tab--left { left: 0; top: 190px; }
  .edge-tab--left::after { right: -3px; }
  .edge-tab--right { right: 0; top: 40px; }
  .edge-tab--right::after { left: -3px; }
  .brand-name {
    position: absolute;
    left: 0;
    top: 134px;
    width: 100%;
    margin: 0;
    text-align: center;
    font-size: 28px;
    font-weight: 600;
    color: var(--gold-text);
  }
</style>
</head>
<body>
<div class="canvas">

  <section class="card card--contact">
    <div class="gold-band gold-band--top"></div>
    <div class="ring-decor" role="img" aria-label="Faint diamond ring illustration"></div>
    <div class="contact-block">
      <h2 class="person-name">DANIEL HARTLEY</h2>
      <p class="person-role">Managing Director</p>
      <p class="contact-line">M: 0417283951</p>
      <p class="contact-line">P: (02) 9163 2748</p>
      <p class="contact-line">info@goldenhourstudio.net.au</p>
      <p class="contact-line">www.goldenhourstudio.net.au</p>
      <p class="address-line">47 Marrowbank Street, Lilyfield NSW 2040</p>
      <div class="social-row">
        <span class="social-dot"></span>
        <span class="social-handle">goldenhourbridals</span>
        <span class="social-dot social-dot--round"></span>
        <span class="social-handle">goldenhourbridals</span>
      </div>
    </div>
    <div class="gold-band gold-band--bottom"></div>
  </section>

  <section class="card card--brand">
    <div class="edge-tab edge-tab--right"></div>
    <h1 class="brand-name">Golden Hour Studios and Film</h1>
    <div class="edge-tab edge-tab--left"></div>
  </section>

</div>
</body>
</html>
```